Used Car Dealer seeks an Amazing Business Card Design

We are looking for a business card design that incorporates our logo and grabs the attention of anyone we give the business card to.

Looking to use the same colors as the logo. Our Logo choice is the black background with Red and Silver/Grey Lettering.

We also would like to see some embossed designs.

Target Market(s)

Used Car Buyers, Automotive, Auto

Industry/Entity Type

Automotive

Contact Information for Business Card

BVEL7K
Gordon Whitlock
482 Tarrow Lane
Suite 207
Roswell, GA 30075
Office (770) 555-0142
Cell (770) 555-0187
bvel7kga@quellmail.com
www.bvel7kga.com

Colors
ffffff
ee3036

Requirements
Must have
• Must include our logo (Black Background with Red and Silver/Grey Lettering)
Nice to have
• Embossed Design. Can be Single or Double Sided.

```html
<!DOCTYPE html>
<html lang="en">
<head>
<meta charset="utf-8">
<title>BVEL7K Business Card</title>
<link href="https://fonts.googleapis.com/css2?family=Open+Sans:wght@400;600&display=swap" rel="stylesheet">
<style>
  :root {
    --bg: #1d1d1f;
    --card: #060606;
    --red: #b81f25;
    --red-bright: #ee3036;
    --white: #ffffff;
    --silver: #c9c9cc;
  }
  * { margin: 0; padding: 0; box-sizing: border-box; }
  html, body { width: 1200px; height: 1200px; overflow: hidden; }
  body {
    background: var(--bg);
    font-family: "Open Sans", Arial, sans-serif;
    display: flex;
    flex-direction: column;
    align-items: center;
    justify-content: center;
    gap: 60px;
  }
  .card {
    position: relative;
    width: 840px;
    height: 480px;
    background: var(--card);
    overflow: hidden;
  }
  .bar { position: absolute; background: var(--red); height: 16px; }
  /* front */
  .card-front .bar-top { top: 22px; left: 150px; width: 480px; }
  .card-front .bar-bottom { bottom: 0; left: 250px; width: 340px; }
  .front-brand {
    position: absolute; top: 150px; left: 0; right: 0;
    display: flex; align-items: center; justify-content: center; gap: 22px;
  }
  .brand-dot { width: 34px; height: 34px; border-radius: 50%; background: var(--red-bright); }
  .brand-name { font-weight: 600; font-size: 96px; color: var(--silver); letter-spacing: 2px; line-height: 1; }
  .front-web {
    position: absolute; top: 320px; left: 0; right: 0; text-align: center;
    color: var(--white); font-size: 28px; letter-spacing: 10px;
  }
  /* back */
  .card-back .bar-top { top: 22px; left: 120px; width: 300px; }
  .back-brand {
    position: absolute; top: 70px; left: 110px;
    display: flex; align-items: center; gap: 14px;
  }
  .back-brand .brand-name { font-size: 58px; }
  .back-brand .brand-dot { width: 22px; height: 22px; }
  .name-band {
    position: absolute; top: 180px; left: 0; width: 840px; height: 100px;
    background: var(--red); color: var(--white);
    padding: 14px 0 0 260px;
  }
  .person-name { font-size: 36px; font-weight: 600; line-height: 1.1; }
  .person-title { font-size: 19px; margin-top: 4px; }
  .contacts {
    position: absolute; top: 310px; left: 260px; right: 30px;
    color: var(--white); font-size: 20px; line-height: 1.75;
  }
  .contacts .label { color: var(--red-bright); margin-right: 6px; }
  .contacts .gap { display: inline-block; width: 40px; }
</style>
</head>
<body>
  <section class="card card-front">
    <div class="bar bar-top"></div>
    <div class="front-brand">
      <span class="brand-dot"></span>
      <span class="brand-name">BVEL7K</span>
    </div>
    <p class="front-web">www.bvel7kga.com</p>
    <div class="bar bar-bottom"></div>
  </section>

  <section class="card card-back">
    <div class="bar bar-top"></div>
    <div class="back-brand">
      <span class="brand-dot"></span>
      <span class="brand-name">BVEL7K</span>
    </div>
    <div class="name-band">
      <p class="person-name">Gordon Whitlock,</p>
      <p class="person-title">MBA, Dipl.-Ing.(FH) Vorstand</p>
    </div>
    <div class="contacts">
      <p><span class="label">A:</span>482 Tarrow Lane, Suite 207, Roswell, GA 30075</p>
      <p><span class="label">P:</span>(770) 555-0142<span class="gap"></span><span class="label">F:</span>(770) 555-0187</p>
      <p><span class="label">E:</span>bvel7kga@quellmail.com</p>
    </div>
  </section>
</body>
</html>
```